KORBALT

The business want a professional looking business card. We have a scetch we will add but want the extra upgrade, and would like more suggestions for variations of our business cards.

```html
<!DOCTYPE html>
<html lang="en">
<head>
<meta charset="utf-8">
<title>KORBALT Business Card</title>
<link rel="stylesheet" href="https://fonts.googleapis.com/css2?family=Tenor+Sans&family=Urbanist:wght@400;500&display=swap">
<style>
  :root {
    --page: #f2f2f2;
    --card-light: #ffffff;
    --card-dark: #000000;
    --gold: #c4992a;
  }
  html, body {
    margin: 0;
    padding: 0;
    width: 1200px;
    height: 1200px;
    overflow: hidden;
    background: var(--page);
  }
  .canvas {
    position: relative;
    width: 1200px;
    height: 1200px;
  }
  .card {
    position: absolute;
    left: 290px;
    width: 620px;
    height: 354px;
    border-radius: 9px;
    overflow: hidden;
  }
  .card--front { top: 222px; background: var(--card-light); }
  .card--back  { top: 624px; background: var(--card-dark); }

  .brand {
    position: absolute;
    display: flex;
    flex-direction: column;
    align-items: center;
    color: var(--gold);
  }
  .brand__dot {
    border-radius: 50%;
    background: var(--gold);
  }
  .brand__name {
    font-family: "Tenor Sans", sans-serif;
    font-weight: 400;
    line-height: 1;
  }
  .card--front .brand {
    left: 0; right: 0; top: 118px;
  }
  .card--front .brand__dot { width: 44px; height: 44px; margin-bottom: 28px; }
  .card--front .brand__name { font-size: 27px; letter-spacing: 9px; margin-right: -9px; }

  .card--back .brand {
    left: 432px; width: 160px; top: 44px;
  }
  .card--back .brand__dot { width: 36px; height: 36px; margin-bottom: 26px; }
  .card--back .brand__name { font-size: 21px; letter-spacing: 6px; margin-right: -6px; }

  .holder {
    position: absolute;
    left: 41px;
    top: 150px;
    color: var(--gold);
  }
  .holder__name {
    font-family: "Tenor Sans", sans-serif;
    font-size: 23px;
    font-weight: 400;
    margin: 0;
    line-height: 1;
    -webkit-text-stroke: 0.6px var(--gold);
  }
  .holder__role {
    font-family: "Urbanist", sans-serif;
    font-size: 19px;
    letter-spacing: 2.6px;
    margin: 6px 0 0;
    line-height: 1;
  }
  .holder__person {
    font-family: "Tenor Sans", sans-serif;
    font-size: 14px;
    margin: 7px 0 0;
    line-height: 1;
    -webkit-text-stroke: 0.3px var(--gold);
  }

  .divider {
    position: absolute;
    left: 43px;
    top: 242px;
  }

  .contacts {
    position: absolute;
    left: 44px;
    top: 287px;
    width: 540px;
    display: grid;
    grid-template-columns: 280px 260px;
    row-gap: 7px;
    font-family: "Urbanist", sans-serif;
    font-size: 18px;
    color: var(--gold);
  }
  .contact {
    display: flex;
    align-items: center;
    height: 18px;
    gap: 13px;
  }
  .contact svg { width: 17px; height: 17px; flex: none; }
</style>
</head>
<body>
<main class="canvas">

  <section class="card card--front">
    <div class="brand">
      <span class="brand__dot"></span>
      <span class="brand__name">KORBALT</span>
    </div>
  </section>

  <section class="card card--back">
    <div class="brand">
      <span class="brand__dot"></span>
      <span class="brand__name">KORBALT</span>
    </div>

    <div class="holder">
      <h1 class="holder__name">KORBALT VARNESTAD</h1>
      <p class="holder__role">CEO &amp; Founder</p>
      <p class="holder__person">ANDERS TOLLEF VARNESTAD</p>
    </div>

    <svg class="divider" width="536" height="12" viewBox="0 0 536 12" aria-hidden="true">
      <rect x="0" y="4.5" width="536" height="3" fill="var(--gold)"/>
      <rect x="145" y="1" width="245" height="10" rx="5" fill="var(--gold)"/>
    </svg>

    <div class="contacts">
      <div class="contact">
        <svg viewBox="0 0 20 20" aria-label="Address">
          <circle cx="10" cy="10" r="10" fill="var(--gold)"/>
          <path d="M10 4.5a3.6 3.6 0 0 0-3.6 3.6c0 2.7 3.6 6.8 3.6 6.8s3.6-4.1 3.6-6.8A3.6 3.6 0 0 0 10 4.5z" fill="var(--card-dark)"/>
          <circle cx="10" cy="8.2" r="1.4" fill="var(--gold)"/>
        </svg>
        <span></span>
      </div>
      <div class="contact">
        <svg viewBox="0 0 20 20" aria-label="Email">
          <circle cx="10" cy="10" r="10" fill="var(--gold)"/>
          <rect x="5" y="6.5" width="10" height="7" rx="0.8" fill="none" stroke="var(--card-dark)" stroke-width="1.2"/>
          <path d="M5.3 7l4.7 3.6L14.7 7" fill="none" stroke="var(--card-dark)" stroke-width="1.2"/>
        </svg>
        <span>korbalt.llc@mailpost.com</span>
      </div>
      <div class="contact">
        <svg viewBox="0 0 20 20" aria-label="Phone">
          <circle cx="10" cy="10" r="10" fill="var(--gold)"/>
          <path d="M4.5 8.6c0-1.6 2.5-2.6 5.5-2.6s5.5 1 5.5 2.6v.8h-2.6V8.2H7.1v1.2H4.5z" fill="var(--card-dark)"/>
          <path d="M6.6 10.2h6.8l1 3.8H5.6z" fill="var(--card-dark)"/>
          <circle cx="10" cy="12" r="1.1" fill="var(--gold)"/>
        </svg>
        <span>004791550274</span>
      </div>
      <div class="contact">
        <svg viewBox="0 0 20 20" aria-label="Website">
          <circle cx="10" cy="10" r="10" fill="var(--gold)"/>
          <g fill="none" stroke="var(--card-dark)" stroke-width="1">
            <circle cx="10" cy="10" r="5"/>
            <ellipse cx="10" cy="10" rx="2.2" ry="5"/>
            <path d="M5 10h10M5.8 7.5h8.4M5.8 12.5h8.4"/>
          </g>
        </svg>
        <span>www.korbalt.llc</span>
      </div>
    </div>
  </section>

</main>
</body>
</html>
```